2 guided dives on the North of Bonaire

2 guided shore dives on the North of Bonaire including authentic local lunch and drinks.
We offer an adventure for experienced divers to discover the dive sites on the north of the island.
Showing you the beauty of the reefs and tasting authentic local cuisine like goat or iguana combined with a stunning view of the surroundings.

Target Market(s)

Divers / tourism

Industry/Entity Type

Tourism / Diving

Font styles to use
Sans Serif

Colors
0054AA
0677BA
7BADD7
CADEEF
E8F1F8
0094D4
00A9DD
6FCCEA
C7EBF8
E9F6FB
F0912C
F2A743
F7CA91
FBE8D2
FDF5EE
EE7325
F08F49
F5BC92
FAE3D3
FDF4ED

Requirements
Must have
• Some of the pictures I uploaded and the food picture / bottom like in the pictures
Nice to have
• inviting to join us on the guided dives
Should not have
• Any picture I didn't provide

```html
<!DOCTYPE html>
<html lang="en">
<head>
<meta charset="utf-8">
<title>North Reef Dive – Guided Dives Flyer</title>
<link rel="stylesheet" href="https://fonts.googleapis.com/css2?family=Caveat+Brush&family=Quicksand:wght@500;700&display=swap">
<style>
  :root{
    --navy:#1a2b52;
    --orange:#f2a743;
    --orange-deep:#f0912c;
    --blue:#0677ba;
    --blue-bright:#1d74d0;
    --badge:#0054aa;
    --white:#ffffff;
    --label:#3a3a3a;
    --page:#ffffff;
  }
  *{box-sizing:border-box;margin:0;padding:0}
  html,body{width:1200px;height:731px;overflow:hidden;background:var(--page)}
  .sheet{position:relative;width:1200px;height:731px;font-family:"Quicksand",sans-serif}
  .side-label{position:absolute;top:38px;width:200px;text-align:center;font:500 26px "Quicksand",sans-serif;color:var(--label)}
  .side-label--front{left:209px}
  .side-label--back{left:771px}

  .flyer{position:absolute;top:74px;width:468px;height:605px;overflow:hidden;background:var(--navy)}
  .flyer--front{left:87px}
  .flyer--back{left:621px}
  .flyer__art{position:absolute;inset:0;width:468px;height:605px}

  .headline{position:absolute;left:38px;top:322px;font:400 44px/1 "Caveat Brush",cursive;color:var(--white);white-space:nowrap}
  .flyer--back .headline{font-size:39px;top:326px}
  .subhead{position:absolute;left:37px;top:381px;font:700 14px/1 "Quicksand",sans-serif;color:var(--orange);white-space:nowrap}
  .perks{position:absolute;left:34px;top:402px;list-style:none}
  .perks li{display:flex;align-items:center;gap:6px;height:20px;font:500 12px/1 "Quicksand",sans-serif;color:var(--white);white-space:nowrap}
  .tick{width:12px;height:12px;flex:none}
  .lunch{position:absolute;left:34px;top:456px;font:500 15px/1 "Quicksand",sans-serif;color:var(--white);white-space:nowrap}
  .venue{position:absolute;left:34px;top:474px;font:400 24px/1 "Caveat Brush",cursive;color:var(--orange);white-space:nowrap}

  .brand{position:absolute;left:14px;top:550px;display:flex;align-items:center;gap:4px}
  .brand__dot{width:22px;height:22px;border-radius:50%;background:var(--orange)}
  .brand__name{font:700 11px/1 "Quicksand",sans-serif;color:var(--white);white-space:nowrap}

  .bar{position:absolute;left:138px;height:19px;display:flex;font:500 12px/19px "Quicksand",sans-serif;color:var(--white);border-radius:3px;overflow:hidden}
  .bar--call{top:540px;width:181px}
  .bar--web{top:563px;width:254px}
  .bar__label{background:var(--orange);color:var(--navy);padding-left:6px;white-space:nowrap}
  .bar--call .bar__label{width:72px}
  .bar--web .bar__label{width:116px}
  .bar__value{flex:1;background:var(--blue-bright);clip-path:polygon(8px 0,100% 0,100% 100%,0 100%);margin-left:-8px;padding-left:12px;display:flex;align-items:center;gap:3px;white-space:nowrap}
  .bar--web .bar__value{padding-left:22px}
  .phone-icon{width:11px;height:11px;flex:none}

  .contact{position:absolute;left:325px;top:541px;list-style:none}
  .contact li{display:flex;align-items:center;gap:3px;font:500 6.4px/9.5px "Quicksand",sans-serif;color:var(--white);white-space:nowrap}
  .contact svg{width:6px;height:6px;flex:none}
  .social{position:absolute;left:397px;top:566px;display:flex;align-items:center;gap:3px}
  .social__dot{width:12px;height:12px;border-radius:50%;background:var(--blue)}
  .social__name{font:500 6.4px/1 "Quicksand",sans-serif;color:var(--white)}
</style>
</head>
<body>
<div class="sheet">
  <div class="side-label side-label--front">front</div>
  <div class="side-label side-label--back">Back</div>

  <!-- English side -->
  <section class="flyer flyer--front">
    <svg class="flyer__art" viewBox="0 0 468 605">
      <defs>
        <linearGradient id="landscapeF" x1="0" y1="0" x2="0" y2="1">
          <stop offset="0" stop-color="#3f86c8"/><stop offset=".38" stop-color="#bcd6ee"/><stop offset=".55" stop-color="#2f6eb3"/><stop offset=".75" stop-color="#5f8a5a"/><stop offset="1" stop-color="#3c6b34"/>
        </linearGradient>
        <linearGradient id="foodF" x1="0" y1="0" x2="1" y2="1">
          <stop offset="0" stop-color="#c98a4a"/><stop offset=".5" stop-color="#d99a3c"/><stop offset="1" stop-color="#8a3a22"/>
        </linearGradient>
        <linearGradient id="reefF" x1="0" y1="0" x2="0" y2="1">
          <stop offset="0" stop-color="#8a2a3a"/><stop offset=".5" stop-color="#2c6f86"/><stop offset="1" stop-color="#1f5c6e"/>
        </linearGradient>
      </defs>
      <rect width="468" height="300" fill="url(#landscapeF)" role="img" aria-label="Photo of a bay with cacti under a blue sky"/>
      <path d="M227,0 C215,120 170,200 105,255 L300,300 L468,420 L468,0 Z" fill="url(#foodF)" role="img" aria-label="Photo of local lunch plates with rice, fries and stew"/>
      <path d="M421,0 C405,130 365,230 296,292 L468,420 L468,0 Z" fill="url(#reefF)" role="img" aria-label="Underwater photo of a seahorse on the reef"/>
      <path d="M227,0 C215,120 170,200 105,255" fill="none" stroke="var(--white)" stroke-width="4"/>
      <path d="M421,0 C405,130 365,230 296,292" fill="none" stroke="var(--white)" stroke-width="4"/>
      <path d="M0,256 C150,244 270,262 340,284" fill="none" stroke="var(--white)" stroke-width="4"/>
      <path d="M0,260 C140,248 280,262 350,288 C260,272 130,270 0,282 Z" fill="var(--orange)"/>
      <path d="M0,282 C130,270 260,272 350,288 C400,315 440,360 468,420 L468,605 L0,605 Z" fill="var(--navy)"/>
      <path d="M330,284 C390,310 440,360 468,418" fill="none" stroke="var(--white)" stroke-width="4"/>
      <circle cx="403" cy="475" r="26" fill="var(--badge)"/>
      <rect x="380" y="505" width="46" height="14" rx="2" fill="var(--white)"/>
    </svg>
    <h1 class="headline">Let us guide you!</h1>
    <p class="subhead">2 guided dives at the North side of Bonaire</p>
    <ul class="perks">
      <li><svg class="tick" viewBox="0 0 12 12"><circle cx="6" cy="6" r="6" fill="var(--orange)"/><path d="M3.3 6.2l1.8 1.8 3.6-3.6" fill="none" stroke="var(--white)" stroke-width="1.5"/></svg>We show you the cool stuff</li>
      <li><svg class="tick" viewBox="0 0 12 12"><circle cx="6" cy="6" r="6" fill="var(--orange)"/><path d="M3.3 6.2l1.8 1.8 3.6-3.6" fill="none" stroke="var(--white)" stroke-width="1.5"/></svg>You just enjoy the dives, we take care of the rest</li>
    </ul>
    <p class="lunch">Authentic local lunch and drinks</p>
    <p class="venue">at Posada Kas Bista</p>
    <div class="brand"><span class="brand__dot"></span><span class="brand__name">North Reef Dive</span></div>
    <div class="bar bar--call"><span class="bar__label">CALL US</span><span class="bar__value"><svg class="phone-icon" viewBox="0 0 12 12"><circle cx="6" cy="6" r="6" fill="var(--white)"/><path d="M4 3.2l1.2 1.4-.6.9c.4.8 1 1.4 1.8 1.8l.9-.6 1.4 1.2-.7 1c-2.4-.3-4.2-2.1-4.6-4.5z" fill="var(--blue-bright)"/></svg>+(599) 700 12 34</span></div>
    <div class="bar bar--web"><span class="bar__label">Visit our Website</span><span class="bar__value">www.northreefdive.com</span></div>
    <ul class="contact">
      <li><svg viewBox="0 0 6 6"><circle cx="3" cy="3" r="3" fill="var(--blue)"/><circle cx="3" cy="2.6" r="1" fill="var(--white)"/></svg>Kaya Koral 12, Kralendijk, Bonaire</li>
      <li><svg viewBox="0 0 6 6"><circle cx="3" cy="3" r="3" fill="var(--blue)"/><rect x="1.6" y="2" width="2.8" height="2" fill="var(--white)"/></svg>info@northreefdive.com</li>
    </ul>
    <div class="social"><span class="social__dot"></span><span class="social__name">@northreefdive</span></div>
  </section>

  <!-- Dutch side -->
  <section class="flyer flyer--back">
    <svg class="flyer__art" viewBox="0 0 468 605">
      <rect width="468" height="300" fill="url(#landscapeF)" role="img" aria-label="Photo of a bay with cacti under a blue sky"/>
      <path d="M227,0 C215,120 170,200 105,255 L300,300 L468,420 L468,0 Z" fill="url(#foodF)" role="img" aria-label="Photo of local lunch plates with rice, fries and stew"/>
      <path d="M421,0 C405,130 365,230 296,292 L468,420 L468,0 Z" fill="url(#reefF)" role="img" aria-label="Underwater photo of a seahorse on the reef"/>
      <path d="M227,0 C215,120 170,200 105,255" fill="none" stroke="var(--white)" stroke-width="4"/>
      <path d="M421,0 C405,130 365,230 296,292" fill="none" stroke="var(--white)" stroke-width="4"/>
      <path d="M0,256 C150,244 270,262 340,284" fill="none" stroke="var(--white)" stroke-width="4"/>
      <path d="M0,260 C140,248 280,262 350,288 C260,272 130,270 0,282 Z" fill="var(--orange)"/>
      <path d="M0,282 C130,270 260,272 350,288 C400,315 440,360 468,420 L468,605 L0,605 Z" fill="var(--navy)"/>
      <path d="M330,284 C390,310 440,360 468,418" fill="none" stroke="var(--white)" stroke-width="4"/>
      <circle cx="403" cy="475" r="26" fill="var(--badge)"/>
      <rect x="380" y="505" width="46" height="14" rx="2" fill="var(--white)"/>
    </svg>
    <h1 class="headline">Laat ons je begeleiden!</h1>
    <p class="subhead">2 gidsduiken in het Noorden van Bonaire</p>
    <ul class="perks">
      <li><svg class="tick" viewBox="0 0 12 12"><circle cx="6" cy="6" r="6" fill="var(--orange)"/><path d="M3.3 6.2l1.8 1.8 3.6-3.6" fill="none" stroke="var(--white)" stroke-width="1.5"/></svg>Wij laten de mooiste dingen zien</li>
      <li><svg class="tick" viewBox="0 0 12 12"><circle cx="6" cy="6" r="6" fill="var(--orange)"/><path d="M3.3 6.2l1.8 1.8 3.6-3.6" fill="none" stroke="var(--white)" stroke-width="1.5"/></svg>Geniet van de duiken, wij regelen de rest</li>
    </ul>
    <p class="lunch">Authentieke lokale lunch met drankjes</p>
    <p class="venue">bij Posada Kas Bista</p>
    <div class="brand"><span class="brand__dot"></span><span class="brand__name">North Reef Dive</span></div>
    <div class="bar bar--call"><span class="bar__label">CALL US</span><span class="bar__value"><svg class="phone-icon" viewBox="0 0 12 12"><circle cx="6" cy="6" r="6" fill="var(--white)"/><path d="M4 3.2l1.2 1.4-.6.9c.4.8 1 1.4 1.8 1.8l.9-.6 1.4 1.2-.7 1c-2.4-.3-4.2-2.1-4.6-4.5z" fill="var(--blue-bright)"/></svg>+(599) 700 12 34</span></div>
    <div class="bar bar--web"><span class="bar__label">Visit our Website</span><span class="bar__value">www.northreefdive.com</span></div>
    <ul class="contact">
      <li><svg viewBox="0 0 6 6"><circle cx="3" cy="3" r="3" fill="var(--blue)"/><circle cx="3" cy="2.6" r="1" fill="var(--white)"/></svg>Kaya Koral 12, Kralendijk, Bonaire</li>
      <li><svg viewBox="0 0 6 6"><circle cx="3" cy="3" r="3" fill="var(--blue)"/><rect x="1.6" y="2" width="2.8" height="2" fill="var(--white)"/></svg>info@northreefdive.com</li>
    </ul>
    <div class="social"><span class="social__dot"></span><span class="social__name">@northreefdive</span></div>
  </section>
</div>
</body>
</html>
```